Law Firm Needs Stationery Design and Business Cards

i would like some fresh new ideas for letterhead. current letterhead is attached. the bottom of the letterhead should have the same content as the bottom of the current letterhead. with the dagger (cross) symbol attached at the beginning and referenced by the two names at the top. see existing letterhead and this will make better sense.

use existing logo and content. nothing overly fancy. i like simple, classy, and refined. does not have to be same font on existing letterhead.

for envelopes, use logo and Raleigh, NC address only

Industry/Entity Type

Business

Contact Information for Business Card

Name: Gordon T. Pelling, Esq.

2846 Vesper Lane, Suite 417
Raleigh, NC 27893

phone 919-555-0143
fax 919-555-0187
cell 919-555-0162

www.pellinglegalgroup.com
gordon@pellinglegalgroup.com

```html
<!DOCTYPE html>
<html lang="en">
<head>
<meta charset="utf-8">
<title>Pelling Law — Business Card</title>
<link href="https://fonts.googleapis.com/css2?family=Mulish:wght@400;700&display=swap" rel="stylesheet">
<style>
  :root {
    --navy: #0b2466;
    --navy-soft: #16307a;
    --slate: #7a7c80;
    --ink: #3c3d40;
    --paper: #ffffff;
    --backdrop: #e3e5e8;
  }
  * { box-sizing: border-box; margin: 0; padding: 0; }
  html, body {
    width: 1200px; height: 1000px; overflow: hidden;
    background: var(--backdrop);
    font-family: "Mulish", Arial, sans-serif;
  }
  .stage {
    width: 1200px; height: 1000px;
    display: flex; flex-direction: column; align-items: center; justify-content: center;
    gap: 56px;
  }
  .card {
    position: relative;
    width: 700px; height: 400px;
    overflow: hidden;
    box-shadow: 0 6px 18px rgba(0,0,0,0.12);
  }

  /* Front */
  .card-front { background: var(--paper); }
  .card-front .edge-top {
    position: absolute; left: 0; top: 0; width: 100%; height: 10px; background: var(--slate);
  }
  .card-front .edge-bottom {
    position: absolute; left: 0; bottom: 0; width: 100%; height: 12px; background: var(--navy);
  }
  .firm-mark {
    position: absolute; left: 60px; top: 96px; width: 230px;
    display: flex; flex-direction: column; align-items: center; gap: 14px;
  }
  .firm-mark .dot {
    width: 64px; height: 64px; border-radius: 50%; background: var(--navy);
  }
  .firm-name {
    color: var(--navy); font-weight: 700; font-size: 28px; letter-spacing: 2px; line-height: 1;
    white-space: nowrap;
  }
  .attorney {
    position: absolute; right: 56px; top: 100px; width: 320px; text-align: right;
  }
  .attorney .name {
    color: var(--navy); font-weight: 700; font-size: 19px; letter-spacing: 0.5px;
    text-transform: uppercase; white-space: nowrap;
  }
  .attorney .credential {
    color: var(--ink); font-size: 13px; margin-top: 3px; white-space: nowrap;
  }
  .contact {
    position: absolute; right: 56px; bottom: 56px; text-align: right;
    color: var(--ink); font-size: 14px; line-height: 1.45; white-space: nowrap;
  }
  .contact .label { color: var(--navy); font-weight: 700; }

  /* Back */
  .card-back { background: var(--navy); }
  .card-back .faint-circle {
    position: absolute; left: 50%; top: 50%;
    width: 300px; height: 300px; margin: -150px 0 0 -150px;
    border-radius: 50%; border: 26px solid var(--navy-soft);
  }
  .card-back .firm-mark-back {
    position: absolute; left: 50%; top: 50%; transform: translate(-50%, -50%);
    color: #ffffff; font-weight: 700; font-size: 40px; letter-spacing: 4px; white-space: nowrap;
  }
</style>
</head>
<body>
  <main class="stage">
    <section class="card card-front" aria-label="Business card front">
      <div class="edge-top"></div>
      <div class="firm-mark">
        <span class="dot"></span>
        <span class="firm-name">PELLING LAW</span>
      </div>
      <div class="attorney">
        <p class="name">Gordon T. Pelling, Esq.</p>
        <p class="credential">Licensed in NC and FL</p>
        <p class="credential">Board CERTIFIED CIVIL TRIAL SPECIALIST</p>
      </div>
      <div class="contact">
        <p><span class="label">T:</span> 919.555.0143</p>
        <p><span class="label">F:</span> 919.555.0187</p>
        <p><span class="label">W:</span> www.pellinglegalgroup.com</p>
        <p>2846 Vesper Lane, Suite 417</p>
        <p>Raleigh, NC 27893</p>
      </div>
      <div class="edge-bottom"></div>
    </section>

    <section class="card card-back" aria-label="Business card back">
      <div class="faint-circle"></div>
      <span class="firm-mark-back">PELLING LAW</span>
    </section>
  </main>
</body>
</html>
```